Need 8.5" x 11" as well as large 11"x17" Posters for our upcoming eventPlease include LOGOs in poster Main logo is Interfaith Youth Council of OCInfo/Content to include:All high school age faith groups are invited to come and join with 150 to 175 other high school students from various faith traditions to participate in the Crossways Teen Assembly of Lark Valley‘s Annual Crossways Teen Roundtable. More than ever, our county and the world needs young leaders who are willing to learn from each other and build stronger communities!FAITH FORUMThe purpose of this Crossways Teen Roundtable is to bring together young people from diverse ethnic, cultural, and religious backgrounds, and to engage them in dialogue. True dialogue is a conversation on a common subject between two or more persons of differing points of view and/or backgrounds. We feel that this commitment to dialogue will affect relationships in a constructive way in our places of worship and in our community.The forum itself involves having eight religiously diverse high school-age students, one adult, and youth leader around each table to discuss common questions. Our youth leaders act as facilitators, but it is stressed that it is the students we want to hear from.
Registration is Required for our BELIEF CIRCLE before February 25th, 2019
FORUM QUESTIONS and rregistration available online at http://ctalv.example/home/belief-fair/

Target Market(s)

Houses of worship, community leaders, High School Students

Industry/Entity Type

Non-Profit

Font styles to use
Serif

Colors
fefcec
f78f20
faa54b
fece3e
3176b5
33a6d7
0592cd
0455a3
f68d4d

Requirements
Must have
• Must Have:
• - Crossways Teen Assembly of Lark Valley's 15th Annual Belief Circle & Fair
• - TEENS EXPRESSING THEIR FAITH THROUGH ART, MUSIC, AND DIALOGUE
• - THIS YEAR'S THEME: "Rivers of Trust"
• - Sunday, March 10th, 2019 1:30pm-6:30pm
• - The Chapel of Harmon Grove Community Fellowship
• - 4817 Mellow Ridge Lane Dunmore Point, CA 93814
• - Email: ctalvorg@brightpost.example
• - Website: CTALV.example
• - Facebook: Crossways Teen Assembly of Lark Valley
• Please include pictures provided
• Logo must be on there and prominent: Crossways Teen assembly of Lark Valley
• second logo should be somewhere on the bottom or back: Tall Harbor Allies
Nice to have
• Descriptions provided in word doc
• Ideally would like Logo and pictures and main info on the front
• - Website: CTALV.example
• On the back have more details about the program and pics if needed

```html
<!DOCTYPE html>
<html lang="en">
<head>
<meta charset="utf-8">
<title>Crossways Teen Assembly of Lark Valley – 15th Annual Belief Circle &amp; Fair</title>
<link rel="stylesheet" href="https://fonts.googleapis.com/css2?family=Montserrat:wght@600;700&family=Questrial&display=swap">
<style>
  :root{
    --orange:#f78f20;
    --orange-soft:#faa54b;
    --blue:#3176b5;
    --blue-deep:#0455a3;
    --link:#0592cd;
    --ink:#2f2f2f;
    --charcoal:#3a3a3a;
    --paper:#ffffff;
    --backdrop:#8f8f8f;
    --partner:#5a9a2e;
    --photo-b:#8c8a86;
  }
  *{margin:0;padding:0;box-sizing:border-box}
  html,body{width:1200px;height:943px;overflow:hidden}
  body{background:var(--backdrop);font-family:"Questrial",Arial,sans-serif;color:var(--ink);position:relative}
  .sheet{position:absolute;background:var(--paper);overflow:hidden}
  .sheet--front{left:48px;top:92px;width:542px;height:768px}
  .sheet--back{left:617px;top:100px;width:538px;height:757px}
  .abs{position:absolute}
  .crowd-wash{position:absolute;left:0;right:0;background:linear-gradient(180deg,rgba(255,255,255,0) 0%,#d9dde2 30%,#c9ced4 100%)}
  .head{font-family:"Montserrat",Arial,sans-serif;font-weight:700}
  .header-title{color:#fff;font-size:13.2px;line-height:18px;white-space:nowrap}
  .header-title .big{font-size:14.6px}
  .header-title b{color:var(--ink);font-weight:700}
  .tagline{color:var(--charcoal);font-size:14.4px;line-height:22px;white-space:nowrap}
  .brand-seal{left:30px;top:26px;width:102px;height:102px;border-radius:50%;border:3px solid var(--ink);display:flex;align-items:center;justify-content:center;text-align:center;font-family:"Montserrat",Arial,sans-serif;font-weight:700;font-size:10px;line-height:12px;color:var(--ink);padding:10px}
  .blue-column{left:347px;top:184px;width:195px;height:530px;background:var(--blue)}
  .photo{position:absolute;border:2px solid #fff;border-radius:10px}
  .forum-title{left:14px;top:216px;font-size:14.5px;line-height:21px;color:var(--ink);white-space:nowrap}
  .forum-title .theme{color:var(--orange)}
  .date-pill{left:14px;top:268px;width:320px;height:21px;border-radius:11px;background:var(--orange);font-size:10.5px;line-height:21px;padding-left:20px;color:var(--ink);white-space:nowrap}
  .venue{left:14px;top:297px;width:320px;text-align:center;font-size:8.6px;color:var(--ink);white-space:nowrap}
  .address{left:14px;top:314px;font-size:9.4px;color:var(--ink);display:flex;align-items:center;gap:5px;white-space:nowrap}
  .copy{font-size:8.2px;line-height:11.3px;text-align:justify;color:var(--ink)}
  .intro{left:15px;top:342px;width:320px}
  .circle-box{left:17px;top:420px;width:316px;height:178px;border:2px solid var(--orange);border-radius:16px;padding:18px 12px 0}
  .circle-box .copy + .copy{margin-top:7px}
  .circle-heading{left:110px;top:409px;padding:0 10px;background:#fff;font-size:12.5px;color:var(--ink)}
  .rsvp{left:20px;top:618px;font-size:10.5px;color:var(--ink)}
  .questions{left:20px;top:637px;font-size:11px;color:var(--ink)}
  .link{left:20px;top:654px;font-size:11px;color:var(--link);text-decoration:underline}
  .footer-line{font-size:9.5px;color:var(--ink);display:flex;align-items:center;gap:5px;white-space:nowrap}
  .dot{width:8px;height:8px;border-radius:50%;background:var(--ink);display:inline-block}
  .back-title{left:0;width:538px;top:32px;text-align:center;color:#fff;font-size:15px;line-height:26px}
  .back-title b{color:var(--ink)}
  .back-date{left:0;width:538px;top:570px;text-align:center;color:var(--blue);font-size:18.5px;white-space:nowrap}
  .back-venue{left:0;width:538px;top:593px;text-align:center;font-size:10.5px;color:var(--ink);white-space:nowrap}
  .back-address{left:40px;top:627px;font-size:14.4px;color:var(--ink);display:flex;align-items:center;gap:6px;white-space:nowrap}
  .partner{left:205px;top:713px;width:150px;text-align:center;font-family:"Montserrat",Arial,sans-serif;font-weight:600;font-size:11px;line-height:12px;color:var(--partner);white-space:nowrap}
</style>
</head>
<body>

<section class="sheet sheet--front">
  <div class="crowd-wash" style="top:330px;bottom:60px" role="img" aria-label="Faded photo of the assembled students filling the hall"></div>

  <svg class="abs" style="left:0;top:0" width="542" height="200" viewBox="0 0 542 200">
    <path d="M0 0H542V166C420 186 300 198 190 190C110 184 50 172 0 160Z" fill="var(--orange)"/>
    <path d="M0 160C50 172 110 184 190 190C300 198 420 186 542 166V178C420 196 300 205 190 198C110 193 50 181 0 170Z" fill="var(--charcoal)"/>
  </svg>

  <div class="abs brand-seal">Crossways Teen Assembly of LV</div>

  <div class="abs head header-title" style="left:147px;top:50px">CROSSWAYS TEEN ASSEMBLY OF LARK VALLEY'S<br><span class="big"><b>15TH</b> ANNUAL BELIEF CIRCLE &amp; FAIR</span></div>
  <div class="abs head tagline" style="left:147px;top:95px">TEENS EXPRESSING THEIR FAITH THROUGH<br>ART, MUSIC, AND DIALOGUE</div>

  <div class="abs blue-column"></div>
  <div class="photo" style="left:372px;top:193px;width:155px;height:113px;background:linear-gradient(135deg,#e9e3dc,#c6403a 60%,#4a6fb0)" role="img" aria-label="Photo of faith symbol banners hung in a row"></div>
  <div class="photo" style="left:372px;top:318px;width:155px;height:112px;background:linear-gradient(135deg,var(--photo-b),#d9b9c2)" role="img" aria-label="Photo of students talking around a round table"></div>
  <div class="photo" style="left:372px;top:442px;width:155px;height:112px;background:linear-gradient(135deg,#6b5a55,#c9b7a6)" role="img" aria-label="Photo of teens performing music on string instruments"></div>
  <div class="photo" style="left:372px;top:566px;width:155px;height:112px;background:linear-gradient(135deg,#f3e6e3,#7a5a44)" role="img" aria-label="Photo of a student playing a drum on stage"></div>

  <div class="abs head forum-title">CROSSWAYS TEEN ROUNDTABLE<br>THIS YEAR'S THEME: "<span class="theme">Rivers of Trust</span>"</div>
  <div class="abs head date-pill">SUNDAY, MARCH 10TH, 2019 1:30PM-6:30PM</div>
  <div class="abs head venue">THE CHAPEL OF HARMON GROVE COMMUNITY FELLOWSHIP</div>
  <div class="abs head address">
    <svg width="10" height="13" viewBox="0 0 10 13"><path d="M5 0C2.2 0 0 2.2 0 5c0 3.5 5 8 5 8s5-4.5 5-8C10 2.2 7.8 0 5 0Zm0 7A2 2 0 1 1 5 3a2 2 0 0 1 0 4Z" fill="var(--ink)"/></svg>
    4817 MELLOW RIDGE LANE DUNMORE POINT, CA 93814
  </div>

  <p class="abs copy intro">All high school age faith groups are invited to come and join with 150 to 175 other high school students from various faith traditions to participate in the Crossways Teen Assembly of Lark Valley's Annual Crossways Teen Roundtable. More than ever, our county and the world needs young leaders who are willing to learn from each other and build stronger communities!</p>

  <div class="abs circle-box">
    <p class="copy">The purpose of this Crossways Teen Roundtable is to bring together young people from diverse ethnic, cultural, and religious backgrounds, and to engage them in dialogue. True dialogue is a conversation on a common subject between two or more persons of differing points of view and/or backgrounds. We feel that this commitment to dialogue will affect relationships in a constructive way in our places of worship and in our community.</p>
    <p class="copy">The forum itself involves having eight religiously diverse high school-age students, one adult, and youth leader around each table to discuss common questions. Our youth leaders act as facilitators, but it is stressed that it is the students we want to hear from.</p>
  </div>
  <div class="abs head circle-heading">BELIEF CIRCLE</div>

  <div class="abs rsvp">RSVP for our BELIEF CIRCLE before February 25th, 2019</div>
  <div class="abs head questions">FORUM QUESTIONS Available online at</div>
  <div class="abs link">http://ctalv.example/home/belief-fair/</div>

  <svg class="abs" style="left:0;top:690px" width="542" height="78" viewBox="0 0 542 78">
    <path d="M0 4C160 22 380 22 542 0V12C380 34 160 34 0 16Z" fill="var(--charcoal)"/>
    <path d="M0 16C160 34 380 34 542 12V78H0Z" fill="var(--orange)"/>
  </svg>
  <div class="abs footer-line" style="left:180px;top:726px">
    <span class="dot"></span>CTALV.example
    <svg style="margin-left:14px" width="12" height="9" viewBox="0 0 12 9"><rect x=".5" y=".5" width="11" height="8" fill="none" stroke="var(--ink)"/><path d="M.5 .5 6 5l5.5-4.5" fill="none" stroke="var(--ink)"/></svg>ctalvorg@brightpost.example
  </div>
  <div class="abs footer-line" style="left:165px;top:745px"><span class="dot"></span>Crossways Teen Assembly of Lark Valley</div>
</section>

<section class="sheet sheet--back">
  <div class="crowd-wash" style="top:500px;bottom:50px" role="img" aria-label="Faded photo of the assembled students filling the hall"></div>

  <svg class="abs" style="left:0;top:0" width="538" height="120" viewBox="0 0 538 120">
    <path d="M0 0H538V70C400 96 200 96 0 80Z" fill="var(--orange)"/>
    <path d="M0 80C200 96 400 96 538 70V82C400 110 200 110 0 92Z" fill="var(--charcoal)"/>
  </svg>
  <div class="abs head back-title">CROSSWAYS TEEN ASSEMBLY OF LARK VALLEY'S<br><b>15TH</b> ANNUAL BELIEF CIRCLE &amp; FAIR</div>

  <div class="photo" style="left:25px;top:151px;width:155px;height:119px;border-color:var(--blue);border-radius:0;background:linear-gradient(135deg,#c0392b,#e7b98a)" role="img" aria-label="Photo of a dancer in traditional dress"></div>
  <div class="photo" style="left:188px;top:151px;width:155px;height:119px;border-color:var(--blue);border-radius:0;background:linear-gradient(135deg,#b8b4ae,#5f5b58)" role="img" aria-label="Photo of students seated at tables in a hall"></div>
  <div class="photo" style="left:352px;top:151px;width:156px;height:119px;border-color:var(--blue);border-radius:0;background:linear-gradient(135deg,#a9a7a3,#4b4744)" role="img" aria-label="Group photo of all participants"></div>
  <div class="photo" style="left:25px;top:278px;width:155px;height:119px;border-color:var(--blue);border-radius:0;background:linear-gradient(135deg,#d9d4cf,#e88a4c)" role="img" aria-label="Photo of markers and name cards on a table"></div>
  <div class="photo" style="left:188px;top:278px;width:155px;height:119px;border-color:var(--blue);border-radius:0;background:linear-gradient(135deg,#b8c9d8,#6d5644)" role="img" aria-label="Photo of youth leaders standing together outdoors"></div>
  <div class="photo" style="left:352px;top:278px;width:156px;height:119px;border-color:var(--blue);border-radius:0;background:linear-gradient(135deg,#c7b39d,#8a6d5a)" role="img" aria-label="Photo of a hand making a sand art piece"></div>
  <div class="photo" style="left:107px;top:405px;width:155px;height:118px;border-color:var(--blue);border-radius:0;background:linear-gradient(135deg,#aeb2b4,#5a5856)" role="img" aria-label="Photo of discussion tables during the forum"></div>
  <div class="photo" style="left:270px;top:405px;width:155px;height:118px;border-color:var(--blue);border-radius:0;background:linear-gradient(135deg,#9aa79c,#4f5a55)" role="img" aria-label="Photo of students listening at round tables"></div>

  <div class="abs head back-date">SUNDAY, MARCH 10TH, 2019 1:30PM-6:30PM</div>
  <div class="abs head back-venue">THE CHAPEL OF HARMON GROVE COMMUNITY FELLOWSHIP</div>
  <div class="abs head back-address">
    <svg width="13" height="17" viewBox="0 0 10 13"><path d="M5 0C2.2 0 0 2.2 0 5c0 3.5 5 8 5 8s5-4.5 5-8C10 2.2 7.8 0 5 0Zm0 7A2 2 0 1 1 5 3a2 2 0 0 1 0 4Z" fill="var(--ink)"/></svg>
    4817 MELLOW RIDGE LANE DUNMORE POINT, CA 93814
  </div>

  <svg class="abs" style="left:0;top:680px" width="538" height="77" viewBox="0 0 538 77">
    <path d="M0 4C160 24 380 24 538 6V16C380 36 160 36 0 16Z" fill="var(--charcoal)"/>
    <path d="M0 16C160 36 380 36 538 16V77H0Z" fill="var(--orange)"/>
  </svg>
  <div class="abs partner">Tall Harbor Allies</div>
  <div class="abs footer-line" style="left:110px;top:735px">
    <svg width="12" height="9" viewBox="0 0 12 9"><rect x=".5" y=".5" width="11" height="8" fill="none" stroke="var(--ink)"/><path d="M.5 .5 6 5l5.5-4.5" fill="none" stroke="var(--ink)"/></svg>ctalvorg@brightpost.example
  </div>
  <div class="abs footer-line" style="left:336px;top:735px"><span class="dot"></span>CTALV.example</div>
</section>

</body>
</html>
```